Business cards & stationery for a cloth diaper retailer
Natural & Organic Baby Products
Bright & Fun-filled
Marisol Treveck
Carvale, MD 20843
info@dotsnugnest.com
www.dotsnugnest.com
My business is web-based so the website address needs to be highlighted on the card.
Services include:
- Cloth diapering workshops
- Newborn rental cloth diaper trial package
- Private In-Home Consults
- Office/Showroom hours

```html
<!DOCTYPE html>
<html lang="en">
<head>
<meta charset="utf-8">
<title>Dot's Snug Nest – Business Card</title>
<link rel="stylesheet" href="https://fonts.googleapis.com/css2?family=Didact+Gothic&family=Montserrat:wght@400;600;700&display=swap">
<style>
  :root {
    --stage: #2b2b2b;
    --card: #ffffff;
    --green: #7cc12e;
    --green-dark: #5e9c19;
    --green-light: #a6d65a;
    --ink: #4a4a4a;
    --muted: #8a8a8a;
    --skin: #f4d2b0;
    --blue: #4aa3df;
  }
  * { margin: 0; padding: 0; box-sizing: border-box; }
  html, body { width: 1200px; height: 871px; overflow: hidden; }
  body {
    background: var(--stage);
    position: relative;
    font-family: "Didact Gothic", "Montserrat", sans-serif;
    color: var(--ink);
  }
  .card {
    position: absolute;
    width: 525px;
    height: 300px;
    border-radius: 14px;
    overflow: hidden;
    background: var(--card);
    box-shadow: 0 10px 30px rgba(0,0,0,.45);
  }

  /* Back side */
  .card-back { left: 70px; top: 120px; }
  .services-panel {
    position: absolute; left: 0; top: 0; bottom: 0; width: 58%;
    background: linear-gradient(135deg, var(--green-light), var(--green) 55%, var(--green-dark));
    color: #fff;
    padding: 70px 0 0 32px;
  }
  .services-title { font-size: 22px; margin-bottom: 14px; }
  .services-list { list-style: none; font-size: 13px; line-height: 1.9; }
  .services-list li::before { content: "•"; margin-right: 8px; }
  .services-web { margin-top: 12px; font-size: 14px; letter-spacing: .5px; }
  .back-illustration {
    position: absolute; right: 20px; top: 25px; width: 220px; height: 250px;
    border-radius: 50% 50% 45% 45%;
    background: radial-gradient(circle at 50% 40%, var(--skin), #e9b98f 60%, rgba(74,163,223,.6));
  }

  /* Front side */
  .card-front { left: 605px; top: 430px; }
  .front-watermark {
    position: absolute; right: -20px; top: 40px; width: 250px; height: 280px;
    border-radius: 50%;
    background: radial-gradient(circle at 50% 40%, rgba(244,210,176,.35), rgba(74,163,223,.12) 70%, transparent 72%);
  }
  .brand { position: absolute; left: 32px; top: 28px; display: flex; align-items: center; gap: 12px; }
  .brand-mascot {
    width: 62px; height: 62px; border-radius: 50%;
    background: radial-gradient(circle at 50% 40%, var(--skin), #e9b98f 65%, var(--blue));
  }
  .brand-name { font-size: 30px; color: var(--green); letter-spacing: .5px; }
  .contact { position: absolute; left: 32px; top: 110px; font-size: 14px; }
  .contact-name { color: var(--green); font-size: 19px; margin-bottom: 4px; }
  .contact-address { color: var(--muted); padding-bottom: 8px; border-bottom: 1px dotted var(--green); width: 190px; margin-bottom: 16px; }
  .contact-row { display: flex; align-items: center; gap: 6px; margin-bottom: 5px; }
  .contact-row svg { width: 12px; height: 12px; fill: var(--green); }
  .contact-row .spacer { width: 22px; }
  .contact-web { color: var(--green); font-family: "Montserrat", sans-serif; font-weight: 700; font-size: 16px; margin-top: 6px; }
</style>
</head>
<body>

  <section class="card card-back">
    <div class="services-panel">
      <h2 class="services-title">Services</h2>
      <ul class="services-list">
        <li>Cloth diapering workshops</li>
        <li>Newborn rental trial package</li>
        <li>Private In-Home Consults</li>
        <li>Office/Showroom hours</li>
      </ul>
      <p class="services-web">www.dotsnugnest.com</p>
    </div>
    <div class="back-illustration" role="img" aria-label="Illustration of a smiling cartoon baby holding a leaf"></div>
  </section>

  <section class="card card-front">
    <div class="front-watermark" role="img" aria-label="Faint large illustration of the cartoon baby mascot"></div>
    <div class="brand">
      <div class="brand-mascot" role="img" aria-label="Small cartoon baby mascot illustration"></div>
      <span class="brand-name">Dot's Snug Nest</span>
    </div>
    <div class="contact">
      <p class="contact-name">Marisol Treveck</p>
      <p class="contact-address">Carvale, MD 20843</p>
      <p class="contact-row">
        <svg viewBox="0 0 24 24" aria-hidden="true"><path d="M6.6 10.8a15 15 0 0 0 6.6 6.6l2.2-2.2c.3-.3.7-.4 1-.2 1.1.4 2.3.6 3.6.6.6 0 1 .4 1 1V20c0 .6-.4 1-1 1A17 17 0 0 1 3 4c0-.6.4-1 1-1h3.5c.6 0 1 .4 1 1 0 1.3.2 2.5.6 3.6.1.3 0 .7-.2 1z"/></svg>
        866-555-0148
        <span class="spacer"></span>
        <svg viewBox="0 0 24 24" aria-hidden="true"><path d="M6.6 10.8a15 15 0 0 0 6.6 6.6l2.2-2.2c.3-.3.7-.4 1-.2 1.1.4 2.3.6 3.6.6.6 0 1 .4 1 1V20c0 .6-.4 1-1 1A17 17 0 0 1 3 4c0-.6.4-1 1-1h3.5c.6 0 1 .4 1 1 0 1.3.2 2.5.6 3.6.1.3 0 .7-.2 1z"/></svg>
        866-555-0148
      </p>
      <p class="contact-row">
        <svg viewBox="0 0 24 24" aria-hidden="true"><path d="M2 5h20v14H2z M2 5l10 8 10-8" fill="none" stroke="#7cc12e" stroke-width="2.4"/></svg>
        info@dotsnugnest.com
      </p>
      <p class="contact-web">www.dotsnugnest.com</p>
    </div>
  </section>

</body>
</html>
```